Passendes Buch-Cover für die Erstveröffentlichung von ,,The Brindlemere Ledgers“ gesucht!
Zielgruppe
Ich möchte mein erstes selbstgeschriebenes Buch über Self Publishing veröffentlichen und suche dafür ein hochwertiges und passendes Buchcover für mein eBook. Die Zielgruppe sind motivierte Leser und Leserinnen jeden Alters!
Inhalt der Story:
Grob umschrieben handelt die Geschichte um ein reiches Familienunternehmen, welches sogenannte Barriques (Eichenfässer) produzieren lässt um darin hochwertigen und teuren Wein zu lagern. Das Unternehmen wird bereits seit über 100 Jahren von den Dorrovicks, einer sehr verschwiegenen und mysteriösen Familie geführt. Sie leben in einer antiken und sehr gepflegten Villa am Ende des Stadtrandes mit einem angrenzenden Eichenwald. Nach dem plötzlichen Tod des Geschäftsführers Ludwig Dorrovick, übernimmt nun sein Sohn, der junge und etwas naive Tobias die Leitung. Erst später stellt sich heraus das die Weinproduktion nicht mit rechten Dingen zugeht und das millionenschwere Unternehmen illegale Geschäfte betreibt. Natürlich gerät dieser Skandal schnell an die Öffentlichkeit und das Familieunternehmen droht zu scheitern. Ab diesem Zeitpunkt tritt Nelly Prescott, Journalistin (Frau am Cover) in das Leben der Dorrovicks um die ungeklärten Fragen aufzudecken.
Aufgabenstellung
Der Buchtitel lautet: The Brindlemere Ledgers (Roman)
Autorname sollte lauten: M.J. Foss (eher klein zu halten)
Text am Cover: Roman
So sollte das Cover ungefähr aussehen:
- Das Buchcover sollte bitte unbedingt dunkel gehalten werden- jedoch keinen komplett schwarzen Hintergrund beinhalten.
- Auf dem Cover befindet sich eine junge Frau ( zwischen 18 und 25 Jahren)- Diese bitte schön passend ins Bild einfügen/ nicht zu nahe aber auch nicht zu weit weg).
- Die Frau sollte sich jedoch nicht direkt mit dem Gesicht den Lesern zeigen! Sie dreht sich etwas schräg.
- Die Frau ist schlank und hat eine gute Figur.
- Die Haare fallen glatt und gehen bis an die Hüften (!Haare können durch einen Lichteinfall LEICHT rötlich schimmern, ist aber kein Muss!). ( Frau sollte wie die Dame im hinzugefügten Bild 3 aussehen).
P.S wenn kein passendes Motiv für die Frau in Frage kommt, kann man sie gerne auch weglassen und mit einer anderen Idee im Mittelpunkt des Covers überzeugen!
Zum Hintergrund:
Hier kann man aus einer der zwei Varianten wählen:
Variante 1:
Der Hintergrund am Cover sollte ungefähr wie das eingespielte Bild 1 aussehen: Es muss nicht zwingend ein Hintergrund (also Haus/Baum etc.) auf dem Cover sein, jedoch sollte man hierbei dann mehr ins Bilddetail gehen und Effekte wie Nebel und Licht und einige dünne Äste einbauen. Die Blätter am Boden gefallen mir auch sehr gut!
Variante 2:
Bei dem eingespielten Bild 2 befindet sich auf dem Cover ein Hintergrund.
Das Mädchen sollte wieder in der Mitte stehen wie oben beschrieben. (Bild 3)
Neben dem Mädchen befinden sich links und rechts Bäume ( Allee/ Eiche) und weiter hinten spiegelt sich durch den Nebel eine Villa ( im sehr klassischen Stil/ hochwertig). Achtung! Die Frau geht nicht auf die Villa zu sondern steht immer noch schräg im Bild. Wie auf dem eingespielten Bild 3!
Zusammenfassung:
- Das Cover sollte letztendlich die junge Fra..

```html
<!DOCTYPE html>
<html lang="en">
<head>
<meta charset="utf-8">
<title>The Brindlemere Ledgers – Book Cover</title>
<link href="https://fonts.googleapis.com/css2?family=Arimo:wght@400;700&display=swap" rel="stylesheet">
<style>
  :root {
    --stage: #2a2745;
    --cover-deep: #0f0d24;
    --cover-navy: #24214a;
    --cover-violet: #3a3560;
    --mist-light: #d9d8a6;
    --mist-green: #8f9660;
    --ember: #9b5a3c;
    --bark: #4b4238;
    --title-cream: #efe8cc;
    --author-gold: #a8925a;
    --label-grey: #8b8896;
  }
  * { margin: 0; padding: 0; box-sizing: border-box; }
  html, body {
    width: 1200px; height: 1055px; overflow: hidden;
    background: var(--stage);
    font-family: "Arimo", Arial, sans-serif;
  }
  .stage { position: relative; width: 1200px; height: 1055px; }

  .front-cover {
    position: absolute; left: 366px; top: 281px;
    width: 329px; height: 490px; overflow: hidden;
    background: linear-gradient(180deg, var(--cover-navy) 0%, var(--cover-deep) 100%);
  }
  .cover-art {
    position: absolute; inset: 0;
    background:
      radial-gradient(ellipse 38% 26% at 50% 44%, var(--mist-light) 0%, var(--mist-green) 40%, transparent 100%),
      radial-gradient(ellipse 60% 22% at 45% 66%, var(--ember) 0%, transparent 100%),
      radial-gradient(ellipse 30% 45% at 18% 40%, var(--bark) 0%, transparent 100%),
      linear-gradient(180deg, var(--cover-navy) 0%, #3b3550 35%, #3a2f45 65%, var(--cover-deep) 85%);
    opacity: .95;
  }
  .cover-label {
    position: absolute; top: 19px; left: 0; right: 0;
    text-align: center; font-size: 15px; letter-spacing: 3px;
    color: var(--label-grey);
  }
  .cover-title {
    position: absolute; top: 280px; left: 0; right: 0;
    text-align: center; color: var(--title-cream);
    font-size: 28px; line-height: 46px; letter-spacing: 9px;
    font-weight: 400; padding-left: 9px;
  }
  .cover-author {
    position: absolute; top: 418px; left: 0; right: 0;
    text-align: center; color: var(--author-gold);
    font-size: 22px; font-weight: 700; letter-spacing: 4px;
  }

  .spine {
    position: absolute; left: 764px; top: 279px;
    width: 57px; height: 494px;
    background: linear-gradient(90deg, var(--cover-navy) 0%, var(--cover-violet) 55%, var(--cover-navy) 100%);
  }
  .spine-title {
    position: absolute; top: 13px; left: 50%;
    transform: translateX(-50%);
    writing-mode: vertical-rl;
    color: var(--title-cream); font-size: 17px; letter-spacing: 6px;
  }
  .spine-author {
    position: absolute; bottom: 14px; left: 50%;
    transform: translateX(-50%);
    writing-mode: vertical-rl;
    color: var(--author-gold); font-size: 8px; font-weight: 700; letter-spacing: 2px;
  }
</style>
</head>
<body>
<main class="stage">
  <section class="front-cover">
    <div class="cover-art" role="img" aria-label="Misty twilight scene: a young woman in a dark dress stands half-turned beneath a large oak tree, fog and warm light glowing around her on a hillside"></div>
    <p class="cover-label">NOVEL</p>
    <h1 class="cover-title">THE<br>BRINDLEMERE<br>LEDGERS</h1>
    <p class="cover-author">M.J. FOSS</p>
  </section>
  <aside class="spine">
    <span class="spine-title">THE BRINDLEMERE LEDGERS</span>
    <span class="spine-author">M.J. FOSS</span>
  </aside>
</main>
</body>
</html>
```